Morvik Construction Business Card

I need a business card design for my company.
We are a construction/machinery company.
I would like to see my logo on the front of the card and my details on the other side
I would like the card to be black or dark grey in colour,with my logo as i send it or modified with a lighter blue colour
I would like to see the design kept fairly simple,but eye catching at the same time
Industry/Entity Type
Business
Colors
00a990
1b1b1b
000000
474747
ececec

```html
<!DOCTYPE html>
<html lang="en">
<head>
<meta charset="UTF-8">
<title>Morvik Construction Business Card</title>
<link rel="stylesheet" href="https://fonts.googleapis.com/css2?family=Source+Sans+3:wght@400;600&display=swap">
<style>
  :root {
    --card-dark: #1b1b1b;
    --band-accent: #00a990;
    --ink-light: #ececec;
    --ink-white: #ffffff;
    --stage: #f4f4f4;
  }
  * { margin: 0; padding: 0; box-sizing: border-box; }
  html, body {
    width: 1200px;
    height: 900px;
    overflow: hidden;
  }
  body {
    position: relative;
    background: var(--stage);
    font-family: "Source Sans 3", "Myriad Pro", sans-serif;
    color: var(--ink-white);
  }
  .card {
    position: absolute;
    background: var(--card-dark);
  }

  /* Details side */
  .card--details {
    left: 78px;
    top: 35px;
    width: 588px;
    height: 362px;
  }
  .brand-band {
    position: absolute;
    top: 38px;
    height: 105px;
    background: var(--band-accent);
  }
  .brand-band--left { left: 0; width: 197px; }
  .brand-band--right { right: 0; width: 196px; }
  .brand-name--small {
    position: absolute;
    left: 197px;
    top: 38px;
    width: 195px;
    height: 105px;
    display: flex;
    align-items: center;
    justify-content: center;
    text-align: center;
    font-weight: 600;
    font-size: 23px;
    line-height: 1.1;
    color: var(--ink-white);
  }
  .contact {
    position: absolute;
    left: 0;
    right: 0;
    top: 166px;
    text-align: center;
  }
  .contact__name {
    font-weight: 600;
    font-size: 22px;
    line-height: 1.1;
    color: var(--ink-white);
  }
  .contact__role {
    font-size: 16px;
    margin-top: 1px;
    color: var(--ink-light);
  }
  .contact__line {
    font-size: 17px;
    display: flex;
    align-items: center;
    justify-content: center;
    gap: 5px;
    line-height: 25px;
    color: var(--ink-light);
  }
  .contact__phone { margin-top: 26px; }
  .contact__address { margin-top: 22px; }
  .icon { width: 12px; height: 12px; fill: var(--band-accent); }

  /* Logo side */
  .card--brand {
    left: 390px;
    top: 507px;
    width: 565px;
    height: 348px;
    border-radius: 14px;
    display: flex;
    align-items: center;
    justify-content: center;
  }
  .brand-name--large {
    font-weight: 600;
    font-size: 50px;
    line-height: 1.05;
    text-align: center;
    letter-spacing: 1px;
    margin-top: 20px;
    color: var(--ink-white);
  }
</style>
</head>
<body>
  <section class="card card--details">
    <div class="brand-band brand-band--left"></div>
    <div class="brand-name brand-name--small">Morvik<br>Construction</div>
    <div class="brand-band brand-band--right"></div>

    <div class="contact">
      <p class="contact__name">Daniel Reeve</p>
      <p class="contact__role">Managing Director</p>
      <p class="contact__line contact__phone">
        <svg class="icon" viewBox="0 0 24 24" aria-hidden="true"><path d="M6.6 10.8a15.1 15.1 0 0 0 6.6 6.6l2.2-2.2c.3-.3.7-.4 1-.2 1.1.4 2.3.6 3.6.6.6 0 1 .4 1 1V20c0 .6-.4 1-1 1A17 17 0 0 1 3 4c0-.6.4-1 1-1h3.5c.6 0 1 .4 1 1 0 1.3.2 2.5.6 3.6.1.3 0 .7-.2 1z"/></svg>
        (044)-318-5206
      </p>
      <p class="contact__line">
        <svg class="icon" viewBox="0 0 24 24" aria-hidden="true"><rect x="2" y="5" width="20" height="14" rx="1"/><path d="M3 6l9 7 9-7" fill="none" stroke="#1b1b1b" stroke-width="2"/></svg>
        info@morvikbuild.com
      </p>
      <p class="contact__line contact__address">12345, Address Goes Here Country Name, 123456</p>
    </div>
  </section>

  <section class="card card--brand">
    <p class="brand-name brand-name--large">Morvik<br>Construction</p>
  </section>
</body>
</html>
```